Simple Floral Service Web-Banner

I need to put a banner add on the members section of a website for an organization in which we are members.

The ad size is 470px x 214px.

I am uploading 4 pictures. 1 is a picture of red roses, and 1 is a picture of a t-shirt. These are 2 major products of ours which need to be incorporated in the banner. I do not have these in higher res or vectorized format, so please work with what you have. I am also uploading our 2 logos, one is for our Canadian company, and one for our American company. Both logos should be included at equal sizes.

The following text should be used:
"Proudly providing top quality roses, and custom commemorative grad t-shirts at over 800 schools."

I am just looking for a simple banner incorporating those pictures and that wording. I don't want something that is overly flashy.

I will monitor the submissions in a timely manner and give you feedback.

```html
<!DOCTYPE html>
<html lang="en">
<head>
<meta charset="utf-8">
<title>Graduation Roses and T-Shirts Banner</title>
<link rel="stylesheet" href="https://fonts.googleapis.com/css2?family=Oswald:wght@500;700&display=swap">
<style>
  :root {
    --frame: #1f2a18;
    --green-light: #b3d846;
    --green-mid: #86b42c;
    --green-dark: #3f7a1a;
    --brand-green: #2f6d1c;
    --white: #ffffff;
    --text-shadow: rgba(20, 50, 10, 0.75);
    --rose-red: #b3161c;
    --rose-leaf: #3e6e22;
    --shirt-green: #7cae2c;
    --shirt-dark: #2c3c1c;
  }
  * { margin: 0; padding: 0; box-sizing: border-box; }
  html, body {
    width: 1200px;
    height: 546px;
    overflow: hidden;
    background: var(--white);
  }
  .banner {
    position: relative;
    width: 1200px;
    height: 546px;
    border: 5px solid var(--frame);
    background: var(--white);
    font-family: "Oswald", "Arial Narrow", sans-serif;
  }
  .hero {
    position: absolute;
    left: 0; top: 0;
    width: 100%;
    height: 405px;
    background: radial-gradient(ellipse 60% 90% at 52% 45%, var(--green-light) 0%, var(--green-mid) 50%, var(--green-dark) 100%);
    border-bottom: 4px solid var(--brand-green);
  }
  .product-roses {
    position: absolute;
    left: 12px; top: 22px;
    width: 300px; height: 365px;
    border-radius: 45% 45% 30% 40%;
    background: radial-gradient(circle at 50% 40%, var(--rose-red) 0%, #8e1015 45%, var(--rose-leaf) 80%, transparent 100%);
  }
  .product-shirts {
    position: absolute;
    right: 20px; top: 95px;
    width: 300px; height: 305px;
    border-radius: 30%;
    background: radial-gradient(circle at 40% 35%, var(--shirt-green) 0%, #557f22 45%, var(--shirt-dark) 80%, transparent 100%);
  }
  .headline {
    position: absolute;
    left: 340px; top: 22px;
    width: 580px;
    text-align: center;
    color: var(--white);
    font-weight: 700;
    text-transform: uppercase;
    line-height: 1.05;
    text-shadow: 2px 3px 4px var(--text-shadow);
  }
  .headline .line { display: block; font-size: 42px; letter-spacing: 0.5px; }
  .headline .emphasis { font-size: 54px; }
  .headline .line-shirts { font-size: 74px; line-height: 1; }
  .footer {
    position: absolute;
    left: 0; bottom: 0;
    width: 100%;
    height: 131px;
    display: flex;
    align-items: center;
    justify-content: space-between;
    padding: 0 22px;
  }
  .brand-name {
    color: var(--brand-green);
    font-weight: 700;
    font-size: 42px;
    line-height: 1;
  }
  .brand-name--right { text-align: right; }
  .brand-divider {
    width: 86px; height: 86px;
    border-radius: 50%;
    background: var(--brand-green);
  }
</style>
</head>
<body>
  <div class="banner">
    <section class="hero">
      <div class="product-roses" role="img" aria-label="Bouquet of red long-stem roses"></div>
      <div class="product-shirts" role="img" aria-label="Two custom commemorative graduation t-shirts in green"></div>
      <h1 class="headline">
        <span class="line">Proudly providing</span>
        <span class="line">Top quality <span class="emphasis">Roses &amp;</span></span>
        <span class="line">Custom commemorative grad</span>
        <span class="line line-shirts">T-Shirts</span>
        <span class="line">At over 800 schools</span>
      </h1>
    </section>
    <footer class="footer">
      <div class="brand-name">Graduate<br>Blooms</div>
      <div class="brand-divider" aria-hidden="true"></div>
      <div class="brand-name brand-name--right">Laureate<br>Blooms</div>
    </footer>
  </div>
</body>
</html>
```